Flyer Template

I need a flyer template for door knocking on properties. Text Boxes need to be editable, with a header and text body. Footer to be my info. Project to be stylized to match my real estate signs and logo art from past projects

```html
<!DOCTYPE html>
<html lang="en">
<head>
<meta charset="utf-8">
<title>Door Knocking Flyer</title>
<link href="https://fonts.googleapis.com/css2?family=Bebas+Neue&family=Source+Sans+3:wght@300;400;600;700&display=swap" rel="stylesheet">
<style>
  :root {
    --red: #e8101f;
    --red-soft: #f0353f;
    --ink: #2b2b2b;
    --grey-text: #3a3a3a;
    --paper: #ffffff;
    --sky: #7f9bc4;
    --lawn: #4f8a34;
  }
  * { margin: 0; padding: 0; box-sizing: border-box; }
  html, body { width: 756px; height: 1200px; overflow: hidden; background: var(--paper); }
  .flyer {
    position: relative; width: 756px; height: 1200px; overflow: hidden;
    background: var(--paper); font-family: "Source Sans 3", Arial, sans-serif; color: var(--grey-text);
  }
  .shapes { position: absolute; inset: 0; }
  .brand {
    position: absolute; left: 36px; top: 60px; width: 150px; text-align: center;
    font-weight: 700; font-size: 27px; line-height: 1.2; color: var(--ink);
  }
  .brand-mark { display: block; width: 40px; height: 40px; margin: 0 auto 14px; background: var(--red); }
  .headline {
    position: absolute; left: 30px; top: 270px;
    font-family: "Bebas Neue", Impact, sans-serif; font-size: 71px; line-height: 67px; color: var(--ink); font-weight: 400;
  }
  .headline .light { color: var(--paper); }
  .section-title {
    position: absolute; left: 30px; font-weight: 700; font-size: 25px; color: var(--ink);
  }
  .section-title em { font-style: normal; color: var(--red); }
  .section-title::after {
    content: ""; position: absolute; left: 0; bottom: -8px; width: 75px; height: 2px; background: var(--red);
  }
  .about-title { top: 612px; }
  .service-title { top: 930px; }
  .about-body {
    position: absolute; left: 30px; top: 660px; width: 380px; font-size: 15.5px; line-height: 20.5px; color: #222;
  }
  .offer {
    position: absolute; left: 470px; top: 590px; width: 250px; text-align: center; color: var(--paper);
  }
  .offer .small { font-size: 24px; line-height: 26px; }
  .offer .big { font-family: "Bebas Neue", Impact, sans-serif; font-size: 76px; line-height: 66px; }
  .price { position: absolute; left: 28px; top: 792px; }
  .price .label { font-size: 33px; font-weight: 300; color: var(--ink); line-height: 36px; }
  .price .amount { font-family: "Bebas Neue", Impact, sans-serif; font-size: 80px; line-height: 72px; color: var(--red); }
  .services {
    position: absolute; left: 30px; top: 988px; width: 560px; list-style: none;
    display: grid; grid-template-columns: 277px 1fr; row-gap: 14px; font-size: 18px; color: #222;
  }
  .services li { display: flex; align-items: center; gap: 10px; white-space: nowrap; }
  .services svg { width: 16px; height: 16px; flex: none; }
  .contact { position: absolute; left: 30px; top: 1088px; color: var(--paper); }
  .contact .row { display: flex; align-items: center; gap: 14px; }
  .contact .phone { font-family: "Bebas Neue", Impact, sans-serif; font-size: 44px; line-height: 44px; }
  .contact .email { font-size: 20px; margin-top: 2px; }
  .contact svg { width: 24px; height: 24px; flex: none; }
  .agent-name {
    position: absolute; left: 352px; top: 1116px; font-weight: 700; font-size: 28px; color: var(--ink); white-space: nowrap;
  }
</style>
</head>
<body>
<div class="flyer">
  <svg class="shapes" width="756" height="1200" viewBox="0 0 756 1200">
    <defs>
      <linearGradient id="house-tones" x1="0" y1="0" x2="0" y2="1">
        <stop offset="0" stop-color="#7f9bc4"/>
        <stop offset="0.55" stop-color="#6d7180"/>
        <stop offset="0.8" stop-color="#5c7a3c"/>
        <stop offset="1" stop-color="#4f8a34"/>
      </linearGradient>
      <linearGradient id="room-tones" x1="0" y1="0" x2="0" y2="1">
        <stop offset="0" stop-color="#e9eaec"/>
        <stop offset="1" stop-color="#7d7a78"/>
      </linearGradient>
      <linearGradient id="agent-tones" x1="0" y1="0" x2="0" y2="1">
        <stop offset="0" stop-color="#e6d3c8"/>
        <stop offset="1" stop-color="#3c4554"/>
      </linearGradient>
    </defs>

    <polygon role="img" aria-label="Photo of a two-storey craftsman house with a lit porch and front lawn at dusk"
      points="362,0 756,0 756,549 348,549 348,390" fill="url(#house-tones)"/>

    <path d="M0,221 H430 Q446,221 442,237 L392,562 Q389,580 372,580 H0 Z" fill="var(--red)"/>
    <path d="M0,221 H430 Q446,221 442,237 L420,380 H0 Z" fill="var(--red-soft)" opacity="0.4"/>

    <path d="M487,580 H714 Q734,580 730,598 L708,732 Q704,752 684,752 H474 Q456,752 459,734 L481,600 Q484,580 487,580 Z" fill="var(--red)"/>

    <polygon points="354,785 541,785 521,911 333,911" fill="none" stroke="var(--red)" stroke-width="2"/>
    <polygon role="img" aria-label="Photo of a bright living room interior" points="359,790 533,790 515,905 339,905" fill="url(#room-tones)"/>
    <polygon points="545,785 732,785 712,911 524,911" fill="none" stroke="var(--red)" stroke-width="2"/>
    <polygon role="img" aria-label="Photo of an open kitchen with dining island" points="550,790 724,790 706,905 530,905" fill="url(#room-tones)"/>

    <path d="M0,1076 H300 C335,1076 350,1120 372,1150 C390,1172 410,1178 440,1180 H756 V1200 H0 Z" fill="var(--red)"/>
    <path d="M318,1080 C345,1090 355,1130 375,1155 C392,1174 410,1180 440,1184" fill="none" stroke="var(--paper)" stroke-width="3"/>

    <path role="img" aria-label="Portrait photo of the agent in a grey blazer, arms crossed"
      d="M578,1200 C588,1150 622,1126 656,1110 L660,1082 C641,1062 636,1004 650,978 C665,948 720,948 735,978 C748,1004 745,1062 722,1086 L726,1106 C744,1114 756,1120 756,1126 V1200 Z" fill="url(#agent-tones)"/>
  </svg>

  <div class="brand"><span class="brand-mark"></span>BRANNOCK<br>REALTY</div>

  <h1 class="headline">The Easiest<br><span class="light">Real Estate</span><br>Door Knocking<br><span class="light">Properties</span></h1>

  <h2 class="section-title about-title">ABOUT THE <em>PROPERTIES</em></h2>
  <p class="about-body">Lorem Ipsum is simply dummy text of the printing and typesetting industry. Lorem Ipsum has been the industry's standard dummy text ever since the 1500s, when an unknown printer took a galley of type and scrambled it to make a type specimen book.</p>

  <div class="offer">
    <div class="small">UP TO</div>
    <div class="big">20% OFF</div>
    <div class="small">LIMITED OFFER</div>
  </div>

  <div class="price">
    <div class="label">PRICE STARTS AT</div>
    <div class="amount">$1,200,000</div>
  </div>

  <h2 class="section-title service-title">OUR BEST <em>SERVICE</em></h2>
  <ul class="services">
    <li><svg viewBox="0 0 16 16"><rect x="1" y="3" width="12" height="12" fill="none" stroke="#e8101f" stroke-width="1.8"/><path d="M4 8 L7 11 L15 2" fill="none" stroke="#e8101f" stroke-width="2"/></svg>Get everything is good price</li>
    <li><svg viewBox="0 0 16 16"><rect x="1" y="3" width="12" height="12" fill="none" stroke="#e8101f" stroke-width="1.8"/><path d="M4 8 L7 11 L15 2" fill="none" stroke="#e8101f" stroke-width="2"/></svg>Our best customer deals ever</li>
    <li><svg viewBox="0 0 16 16"><rect x="1" y="3" width="12" height="12" fill="none" stroke="#e8101f" stroke-width="1.8"/><path d="M4 8 L7 11 L15 2" fill="none" stroke="#e8101f" stroke-width="2"/></svg>75% off is every sales</li>
    <li><svg viewBox="0 0 16 16"><rect x="1" y="3" width="12" height="12" fill="none" stroke="#e8101f" stroke-width="1.8"/><path d="M4 8 L7 11 L15 2" fill="none" stroke="#e8101f" stroke-width="2"/></svg>Best business services provide</li>
  </ul>

  <div class="contact">
    <div class="row phone">
      <svg viewBox="0 0 24 24"><path d="M6 2 L9 2 L10.5 7 L8 9 C9.5 12 12 14.5 15 16 L17 13.5 L22 15 V18 C22 20 20 22 18 22 C9 21 3 15 2 6 C2 4 4 2 6 2 Z" fill="#fff"/></svg>
      555-214-0187
    </div>
    <div class="row email">
      <svg viewBox="0 0 24 24"><rect x="2" y="5" width="20" height="14" fill="#fff"/><path d="M2 5 L12 13 L22 5" fill="none" stroke="#e8101f" stroke-width="1.6"/></svg>
      JBRANNOCK@MAILBOX.COM
    </div>
  </div>

  <div class="agent-name">Jordan Brannock</div>
</div>
</body>
</html>
```